Business Card for Voltrix

Horizontal business card for voltrix, the electrical contractor.
clean and professional looking, using company branding and colours.
I also want the blue in the logo and wording to be made a more 'electric' blue and the grey 'Voltrix' to be slightly darker.

Pleas use the following contact details:

Peter Alwick
Owner

t: 01632 960581
m: 07700 900316
e: peter@voltrix-wiring.co.uk

www.voltrix-wiring.co.uk

Industry/Entity Type

Electrical

Font styles to use
Sans Serif

```html
<!DOCTYPE html>
<html lang="en">
<head>
<meta charset="utf-8">
<title>Voltrix – Business Card</title>
<link rel="stylesheet" href="https://fonts.googleapis.com/css2?family=Michroma&family=Tinos&display=swap">
<style>
  :root {
    --card-bg: #05060c;
    --electric-blue: #5cd2ff;
    --tagline-blue: #3fcbea;
    --mark-grey: #3e3f44;
    --contact-white: #ffffff;
    --bolt-core: rgba(190, 200, 255, 0.85);
    --bolt-glow: rgba(98, 86, 230, 0.55);
    --bolt-fade: rgba(40, 30, 120, 0);
    --coil-light: rgba(150, 228, 236, 0.75);
    --coil-mid: rgba(90, 200, 212, 0.55);
    --coil-fade: rgba(60, 170, 190, 0);
  }
  * { margin: 0; padding: 0; box-sizing: border-box; }
  html, body {
    width: 1200px;
    height: 640px;
    overflow: hidden;
    background: var(--card-bg);
  }
  .card {
    position: relative;
    width: 1200px;
    height: 640px;
    background: var(--card-bg);
    overflow: hidden;
  }
  .wordmark {
    position: absolute;
    left: 28px;
    top: 4px;
    width: 1164px;
    height: 110px;
  }
  .wordmark text {
    font-family: "Michroma", sans-serif;
    font-size: 118px;
    fill: var(--electric-blue);
  }
  .lightning-art {
    position: absolute;
    left: 0;
    top: 150px;
    width: 1200px;
    height: 330px;
    background:
      radial-gradient(ellipse 48% 22% at 50% 48%, var(--bolt-core), rgba(150, 140, 255, 0.35) 45%, var(--bolt-fade) 100%),
      radial-gradient(ellipse 55% 48% at 50% 50%, var(--bolt-glow), var(--bolt-fade) 100%);
  }
  .coil-art {
    position: absolute;
    top: 240px;
    width: 200px;
    height: 400px;
    background: linear-gradient(180deg, var(--coil-fade) 0%, var(--coil-light) 18%, var(--coil-mid) 60%, var(--coil-fade) 100%);
  }
  .coil-art.left { left: 0; }
  .coil-art.right { right: 0; }
  .brand-mark {
    position: absolute;
    left: 0;
    top: 262px;
    width: 1200px;
    text-align: center;
    font-family: "Michroma", sans-serif;
    font-size: 46px;
    line-height: 1;
    color: var(--mark-grey);
  }
  .contact, .person {
    position: absolute;
    font-family: "Tinos", serif;
    color: var(--contact-white);
  }
  .contact { font-size: 29px; line-height: 1; }
  .contact.email { left: 10px; top: 117px; }
  .contact.phone { left: 14px; top: 597px; }
  .contact.mobile { right: 12px; top: 597px; }
  .contact.web { left: 0; width: 1200px; text-align: center; top: 572px; font-size: 32px; }
  .person {
    right: 4px;
    top: 132px;
    width: 264px;
    text-align: center;
    font-size: 37px;
    line-height: 54px;
  }
  .tagline {
    position: absolute;
    left: 0;
    width: 1200px;
    top: 476px;
    text-align: center;
    font-family: "Michroma", sans-serif;
    font-size: 32px;
    letter-spacing: 1px;
    color: var(--tagline-blue);
  }
</style>
</head>
<body>
  <div class="card">
    <div class="lightning-art" role="img" aria-label="Violet electric arcs of lightning stretching across the card"></div>
    <div class="coil-art left" role="img" aria-label="Glowing cyan electrode coil illustration on the left"></div>
    <div class="coil-art right" role="img" aria-label="Glowing cyan electrode coil illustration on the right"></div>

    <svg class="wordmark" viewBox="0 0 1164 110" aria-label="Voltrix">
      <text x="0" y="98" textLength="1164" lengthAdjust="spacingAndGlyphs">VOLTRIX</text>
    </svg>

    <p class="brand-mark">VOLTRIX</p>

    <p class="contact email">e: peter@voltrix-wiring.co.uk</p>
    <div class="person">
      <p class="person-name">Peter Alwick</p>
      <p class="person-role">Owner</p>
    </div>

    <p class="tagline">THE ELECTRICAL CONTRACTOR</p>

    <p class="contact web">www.voltrix-wiring.co.uk</p>
    <p class="contact phone">t: 01632 960581</p>
    <p class="contact mobile">m: 07700 900316</p>
  </div>
</body>
</html>
```